Velvet Hounds Website - Boutique online pet store for both owners, their homes and their dogs

I need a high end online store for the sale of dog products (collars, leashes, coats etc), products for their owners (pyjamas, cosmetic bags, pencil cases, gift wrapping paper, greeting cards etc) and the owners home (ring holders, cushion covers, throws etc).

Please peruse the following website for a vauge idea of slightly similar stores:

Mybeaglecorner.example.com.au
Pawtrailhub.example.com.au
Terriertreats.example.com.au
Tallpup.example.co.za

Please keep in mind these are breed specific sites. I intend for the business to sell to trending dog breeds, for example, currently in Australia, French Bulldogs and Dachshunds are trending; therefore this will be the business's current focus.

I also intend for this website to be more elegant and refined than the websites mentioned above. Similar to top names brands, with a hint of cuteness to appeal to the animal lover within customers.

Target Market(s)

Velvet Hounds' target market is majority females, late 20's - 40's, either single, in a relationship, or with children who have left the home. They own small and pampered dogs and treat these dogs like their children. They will have a high disposable income.

I want the brand to attract elitist clientele. Comment has been made that people mightn't be able to spell Velvet when searching for the website; those are not the type of customers I want to attract. I think it may be difficult to encapsulate these two target ideas into the brand; I'd like is to appeal to both the 'Melbourne Socialite' and the Noosa stereotype of "I'm too cool to show it, but I really care what you think"

The products will be, for the most part, unique to the market, a few examples include:

custom hand made collars and leads reflecting current human fashion trends;
leather coats for dogs;
flannel pyjamas for dog;
chef's hats for dogs;
furniture which incorporates dogs beds (blanket box, coffee table, bedside table)
bags, cushions, throw rugs, pyjamas made from various dog print fabrics;
fine leather handbags and purses with various and discreet dog themed embellishments;
custom gift wrapping paper etc etc

Amazing customer service and high quality are two of the core values of Velvet Hounds.

The business will be run through the website as well as high-end markets around Brisbane, Gold Coast and Sunshine Coast.

Colors
eea4c8
ffffff
e34197

Requirements
Must have
• MUST BE FULLY OPERATIONAL ON COMPLETION. I own the domain name www.velvethounds.example.com.au. Needs to be functioning on this domain with an operational online store using PayPal.
• Must also be mobile friendly.
• Pages:
• For your pup (shopping page)
• For your home (shopping page)
• For you (shopping page)
• Stationery
• Contact us
• I am open to better and more creative page names.
• MUST have an easy to operate back end that I can use to update products as and when required.

```html
<!DOCTYPE html>
<html lang="en">
<head>
<meta charset="utf-8">
<title>Velvet Hounds — Boutique for Dogs, Homes and Owners</title>
<link href="https://fonts.googleapis.com/css2?family=Montserrat:wght@400;500;600&family=Raleway:wght@300;400;500&family=Great+Vibes&display=swap" rel="stylesheet">
<style>
:root{
  --pink:#e34197;
  --pink-soft:#eea4c8;
  --pink-mid:#ef6aa8;
  --white:#ffffff;
  --ink:#1d1d1d;
  --text:#3a3a3a;
  --muted:#777777;
  --line:#cfcfcf;
  --bar:#efefef;
  --tile:#eeeeee;
  --footer:#ececec;
  --teal:#0f3a44;
}
*{box-sizing:border-box;margin:0;padding:0}
html,body{width:1200px;height:2469px;overflow:hidden;background:var(--white)}
body{position:relative;font-family:"Raleway",Arial,sans-serif;color:var(--text)}
.abs{position:absolute}
.caps{font-family:"Montserrat",Arial,sans-serif;text-transform:uppercase}

/* top bar */
.top-bar{left:0;top:0;width:1200px;height:36px;background:var(--bar);border-bottom:2px solid #e2e2e2}
.top-bar .links{top:11px;font-size:11px;color:#555;letter-spacing:.5px;word-spacing:2px}
.top-bar .links span{margin:0 14px;color:#999}

/* header */
.logo{left:102px;top:70px;display:flex;align-items:center;gap:12px}
.logo .mark{width:34px;height:34px;background:var(--pink)}
.logo .name{font-family:"Montserrat",Arial,sans-serif;font-weight:600;font-size:25px;color:var(--ink);letter-spacing:.5px;line-height:1}
.search{left:815px;top:46px;width:185px;height:33px;border:1px solid #dcdcdc;border-radius:17px;background:var(--white)}
.search .ph{left:14px;top:9px;font-size:11px;color:#aaa}
.search .btn{right:-1px;top:-1px;width:33px;height:33px;border-radius:50%;background:var(--pink-mid)}
.cart-tag{left:1017px;top:36px;width:56px;height:58px}
.cart-tag .lbl{left:0;top:26px;width:56px;text-align:center;font-family:"Montserrat",sans-serif;font-size:9px;font-weight:600;color:var(--ink)}
.nav{top:130px;font-size:13px;font-weight:500;color:var(--ink);letter-spacing:.3px;transform:translateX(-50%);white-space:nowrap}
.nav.active{color:var(--pink-mid)}

/* hero */
.hero{left:0;top:165px;width:1200px;height:510px;background:linear-gradient(100deg,#5a5142 0%,#6e6a55 30%,#3f5a3a 55%,#7c7f6c 80%,#8a8a86 100%)}
.hero .script{font-family:"Great Vibes",cursive;color:var(--white);line-height:1}
.hero .custom{left:189px;top:345px;font-size:30px}
.hero .handmade{left:145px;top:355px;font-size:66px;color:#f3b9d6}
.hero .collars{left:240px;top:415px;font-size:66px;color:#dfe6ef}
.hero .tagline{left:158px;top:497px;font-size:17px;color:var(--white);font-weight:400}
.hero .shop{left:224px;top:533px;font-family:"Montserrat",sans-serif;font-weight:600;font-size:15px;color:#111}

/* promo band */
.promo-band{left:0;top:675px;width:1200px;height:238px;background:#3a3632}
.promo{top:691px;width:563px;height:204px;border:2px solid var(--white)}
.promo.coats{left:20px;background:linear-gradient(90deg,#6d6a66,#a98a70 55%,#d7c7b6)}
.promo.pyjamas{left:617px;background:linear-gradient(90deg,#d9cfc2,#cdbfae 55%,#b98a72)}
.promo .title{left:20px;top:72px;font-size:29px;font-weight:400;letter-spacing:1px}
.promo .sub{left:20px;top:106px;font-size:11px}
.promo .btn{left:20px;top:126px;width:106px;height:34px;font-family:"Montserrat",sans-serif;font-size:11px;font-weight:600;color:var(--white);text-align:center;line-height:34px;letter-spacing:.5px}
.coats .title,.coats .sub{color:var(--white)}
.coats .btn{background:var(--teal);border:1px solid var(--white)}
.pyjamas .title,.pyjamas .sub{color:#333}
.pyjamas .btn{background:var(--pink-mid)}

/* product sections */
.sec-head{left:99px}
.sec-head .bar{left:0;top:0;width:3px;height:28px;background:linear-gradient(var(--ink) 50%,var(--pink-mid) 50%)}
.sec-head .kicker{left:14px;top:0;font-size:9px;color:var(--pink-mid)}
.sec-head .title{left:14px;top:12px;font-size:14px;font-weight:600;color:var(--ink)}
.arrow{width:28px;height:28px;border:1px solid #ddd;border-radius:50%;background:var(--white)}
.tile{width:226px;height:210px;background:var(--tile)}
.tile .art{left:50%;top:50%;transform:translate(-50%,-50%);border-radius:14px}
.pname{width:150px;font-size:11.5px;line-height:17px;color:var(--ink)}
.price{width:100px;text-align:right;font-family:"Montserrat",sans-serif;font-size:20px;font-weight:500;color:var(--ink)}
.add{width:226px;height:27px;border-top:1px solid var(--line);border-bottom:1px solid var(--line);text-align:center;line-height:26px;font-size:12.5px;font-weight:500;color:var(--ink);letter-spacing:.6px}
.add b{font-size:15px;margin-right:6px}

/* news band */
.news-band{left:0;top:1761px;width:1200px;height:382px;background:linear-gradient(90deg,#4b4542 0%,#5b5450 45%,#6a625b 70%,#54504c 100%)}
.news-shade{left:0;top:1761px;width:1200px;height:382px;background:rgba(30,28,28,.35)}
.band-title{top:1796px;font-size:15px;color:var(--pink-mid);letter-spacing:.5px}
.band-rule{top:1840px;width:55px;height:1px;background:rgba(255,255,255,.6)}
.avatar{width:70px;height:70px;background:linear-gradient(#c8b8a8,#8e7b6c)}
.post-date{font-family:"Montserrat",sans-serif;font-weight:600;font-size:13px;color:var(--white)}
.post-text{width:360px;font-size:12px;line-height:20px;color:#eee}
.dots{display:flex;gap:9px}
.dots i{width:8px;height:8px;border-radius:50%;border:1px solid #ccc;display:block}
.dots i.on{background:var(--pink-mid);border-color:var(--pink-mid)}
.quote-box{left:606px;top:1880px;width:479px;height:117px;border:1px solid rgba(255,255,255,.75)}
.quote-box .icon{left:22px;top:20px;width:38px;height:38px;border-radius:50%;background:rgba(255,255,255,.25);border:1px solid rgba(255,255,255,.6)}
.quote-box .txt{left:68px;top:18px;width:395px;font-size:12.5px;line-height:20px;color:#f2f2f2}
.client-av{left:639px;top:2021px;width:62px;height:62px;border-radius:50%;border:3px solid var(--white);background:linear-gradient(#d8c1ae,#a78e78)}
.client-name{left:719px;top:2045px;font-family:"Montserrat",sans-serif;font-size:11px;color:var(--white)}

/* footer */
.footer{left:0;top:2143px;width:1200px;height:285px;background:var(--footer)}
.f-head{top:2184px;font-family:"Montserrat",sans-serif;font-weight:600;font-size:13px;color:var(--ink)}
.f-text{font-size:12.5px;line-height:24px;color:#666}
.f-div{top:2180px;width:1px;height:205px;background:#d6d6d6}
.f-links{list-style:none;font-size:11px;color:#555;line-height:20.5px}
.f-links li::before{content:"•";color:var(--pink-mid);margin-right:7px;font-size:9px}
.social{top:2337px;width:14px;height:14px;border-radius:50%;background:#c5c5c5}
.email{left:802px;top:2286px;width:281px;text-align:center;font-size:12px;color:#666}
.email-line{left:802px;top:2310px;width:281px;height:1px;background:#cfcfcf}
.subscribe{left:894px;top:2334px;width:95px;height:30px;border:1px solid #cfcfcf;border-radius:15px;text-align:center;line-height:28px;font-family:"Montserrat",sans-serif;font-size:9px;letter-spacing:1px;color:#444}

/* bottom bar */
.bottom{left:0;top:2428px;width:1200px;height:41px;background:var(--white)}
.copy{left:99px;top:2441px;font-size:11.5px;color:#555}
.copy em{font-style:normal;color:var(--pink-mid)}
.pay{top:2438px;width:30px;height:20px;border-radius:2px}
</style>
</head>
<body>

<!-- top bar -->
<div class="abs top-bar">
  <div class="abs links caps" style="left:100px">My Account<span>|</span>Wish List (0)<span>|</span>Checkout<span>|</span>About Us</div>
  <div class="abs links caps" style="right:100px">Login<span>|</span>Register</div>
</div>

<!-- header -->
<div class="abs logo"><div class="mark"></div><div class="name">VELVET HOUNDS</div></div>
<div class="abs search">
  <div class="abs ph">Search...</div>
  <div class="abs btn">
    <svg width="33" height="33" viewBox="0 0 33 33"><circle cx="15" cy="15" r="5" fill="none" stroke="#fff" stroke-width="2"/><line x1="19" y1="19" x2="23" y2="23" stroke="#fff" stroke-width="2"/></svg>
  </div>
</div>
<div class="abs cart-tag">
  <svg class="abs" width="56" height="58" viewBox="0 0 56 58"><path d="M0 0H56V58L28 46L0 58Z" fill="#ef6aa8"/><path d="M20 10h3l3 9h9l2-6H25" fill="none" stroke="#fff" stroke-width="1.6"/><circle cx="27" cy="22" r="1.5" fill="#fff"/><circle cx="34" cy="22" r="1.5" fill="#fff"/></svg>
  <div class="abs lbl">(0) Item</div>
</div>
<div class="abs nav caps active" style="left:374px">Home</div>
<div class="abs nav caps" style="left:502px">For Your Pup</div>
<div class="abs nav caps" style="left:658px">For Your Home</div>
<div class="abs nav caps" style="left:798px">For You</div>
<div class="abs nav caps" style="left:925px">Stationery</div>
<div class="abs nav caps" style="left:1057px">Contact Us</div>

<!-- hero -->
<div class="abs hero" role="img" aria-label="Photo of three green shamrock-print dog collars stacked on a white pedestal, blurred garden behind"></div>
<div class="abs hero" style="background:none">
  <div class="abs script custom" style="top:180px">Custom</div>
  <div class="abs script handmade" style="top:190px">Handmade</div>
  <div class="abs script collars" style="top:250px">Collars</div>
  <div class="abs tagline" style="top:332px">Current Human Fashion Trends</div>
  <svg class="abs" style="left:153px;top:372px" width="215" height="16" viewBox="0 0 215 16"><line x1="0" y1="8" x2="62" y2="8" stroke="#111" stroke-width="1.2"/><line x1="153" y1="8" x2="215" y2="8" stroke="#111" stroke-width="1.2"/></svg>
  <div class="abs shop" style="top:368px">Shop Now</div>
</div>

<!-- promo band -->
<div class="abs promo-band"></div>
<div class="abs promo coats" role="img" aria-label="Photo of a brown and white puppy in a coat">
  <div class="abs title caps" style="font-family:Raleway,sans-serif">Leather Coats</div>
  <div class="abs sub caps">For Dogs</div>
  <div class="abs btn caps">Shop Now</div>
</div>
<div class="abs promo pyjamas" role="img" aria-label="Photo of two pugs wearing red and blue knitted pyjamas">
  <div class="abs title caps" style="font-family:Raleway,sans-serif">Flannel Pyjamas</div>
  <div class="abs sub caps">For Dogs</div>
  <div class="abs btn caps">Shop Now</div>
</div>

<!-- latest products -->
<div class="abs sec-head" style="top:975px">
  <div class="abs bar"></div>
  <div class="abs kicker caps">Latest</div>
  <div class="abs title caps">Products</div>
</div>
<div class="abs arrow" style="left:1041px;top:980px"><svg width="28" height="28" viewBox="0 0 28 28"><path d="M16 10l-4 4 4 4" fill="none" stroke="#333" stroke-width="1.5"/></svg></div>
<div class="abs arrow" style="left:1075px;top:980px"><svg width="28" height="28" viewBox="0 0 28 28"><path d="M12 10l4 4-4 4" fill="none" stroke="#333" stroke-width="1.5"/></svg></div>

<div class="abs tile" style="left:99px;top:1024px" role="img" aria-label="Product photo of coloured leather dog collars"><div class="abs art" style="width:150px;height:70px;background:linear-gradient(90deg,#e0478f,#3a9a8a,#c99a3a)"></div></div>
<div class="abs tile" style="left:360px;top:1024px" role="img" aria-label="Product photo of a small terrier in a grey coat"><div class="abs art" style="width:140px;height:110px;background:linear-gradient(#8a7a66,#5a5550)"></div></div>
<div class="abs tile" style="left:620px;top:1024px" role="img" aria-label="Product photo of a small dog in pink pyjamas"><div class="abs art" style="width:110px;height:150px;background:linear-gradient(#d8c2a8,#e6a8cc)"></div></div>
<div class="abs tile" style="left:876px;top:1024px" role="img" aria-label="Product photo of a floral bow-tie dog collar"><div class="abs art" style="width:140px;height:90px;background:linear-gradient(90deg,#e9a3b6,#a6c38a,#e9a3b6)"></div></div>

<div class="abs pname" style="left:99px;top:1243px">Ut wisi enim ad minim veniam, quis nostrud</div>
<div class="abs price" style="left:225px;top:1250px">$07.56</div>
<div class="abs pname" style="left:360px;top:1243px">Ut wisi enim ad minim veniam, quis nostrud</div>
<div class="abs price" style="left:486px;top:1250px">$22.56</div>
<div class="abs pname" style="left:620px;top:1243px">Ut wisi enim ad minim veniam, quis nostrud</div>
<div class="abs price" style="left:746px;top:1250px">$105.0</div>
<div class="abs pname" style="left:876px;top:1243px">Ut wisi enim ad minim veniam, quis nostrud</div>
<div class="abs price" style="left:1002px;top:1250px">$28.56</div>

<div class="abs add caps" style="left:99px;top:1295px"><b>+</b>Add to Cart</div>
<div class="abs add caps" style="left:360px;top:1295px"><b>+</b>Add to Cart</div>
<div class="abs add caps" style="left:620px;top:1295px"><b>+</b>Add to Cart</div>
<div class="abs add caps" style="left:876px;top:1295px"><b>+</b>Add to Cart</div>

<!-- featured products -->
<div class="abs sec-head" style="top:1363px">
  <div class="abs bar"></div>
  <div class="abs kicker caps">Featured</div>
  <div class="abs title caps">Products</div>
</div>
<div class="abs arrow" style="left:1041px;top:1368px"><svg width="28" height="28" viewBox="0 0 28 28"><path d="M16 10l-4 4 4 4" fill="none" stroke="#333" stroke-width="1.5"/></svg></div>
<div class="abs arrow" style="left:1075px;top:1368px"><svg width="28" height="28" viewBox="0 0 28 28"><path d="M12 10l4 4-4 4" fill="none" stroke="#333" stroke-width="1.5"/></svg></div>

<div class="abs tile" style="left:99px;top:1412px" role="img" aria-label="Product photo of a white dog in a black leather jacket and cap"><div class="abs art" style="width:140px;height:130px;background:linear-gradient(#2b2b2b,#d8d8d8)"></div></div>
<div class="abs tile" style="left:360px;top:1412px" role="img" aria-label="Product photo of black and red fur-trimmed dog coats"><div class="abs art" style="width:130px;height:120px;background:linear-gradient(90deg,#1f2630,#c4242a)"></div></div>
<div class="abs tile" style="left:620px;top:1412px" role="img" aria-label="Product photo of a cream cushion with an orange dachshund print"><div class="abs art" style="width:150px;height:100px;background:linear-gradient(#f4ead8,#f0c79a)"></div></div>
<div class="abs tile" style="left:876px;top:1412px" role="img" aria-label="Product photo of red dog pyjamas and a terrier print cushion"><div class="abs art" style="width:160px;height:100px;background:linear-gradient(90deg,#c42834,#c4c4c0)"></div></div>

<div class="abs pname" style="left:99px;top:1635px">Ut wisi enim ad minim ve with Cap pan malse</div>
<div class="abs price" style="left:225px;top:1643px">$28.56</div>
<div class="abs pname" style="left:360px;top:1635px">Ut wisi enim ad minim veniam, quis nostrud</div>
<div class="abs price" style="left:486px;top:1643px">$18.56</div>
<div class="abs pname" style="left:620px;top:1635px">Ut wisi enim ad minim veniam, quis nostrud</div>
<div class="abs price" style="left:746px;top:1643px">$14.56</div>
<div class="abs pname" style="left:876px;top:1635px">Ut wisi enim ad minim veniam, quis nostrud</div>
<div class="abs price" style="left:1002px;top:1643px">$14.56</div>

<div class="abs add caps" style="left:99px;top:1689px"><b>+</b>Add to Cart</div>
<div class="abs add caps" style="left:360px;top:1689px"><b>+</b>Add to Cart</div>
<div class="abs add caps" style="left:620px;top:1689px"><b>+</b>Add to Cart</div>
<div class="abs add caps" style="left:876px;top:1689px"><b>+</b>Add to Cart</div>

<!-- news & testimonials -->
<div class="abs news-band" role="img" aria-label="Dim photo of a French bulldog on a wooden deck"></div>
<div class="abs news-shade"></div>

<div class="abs band-title caps" style="left:102px">News &amp; Blog</div>
<div class="abs band-rule" style="left:102px"></div>
<div class="abs avatar" style="left:100px;top:1881px" role="img" aria-label="Portrait photo of blog author"></div>
<div class="abs post-date" style="left:186px;top:1886px">Mar 18, 2016</div>
<div class="abs post-text" style="left:186px;top:1906px">Lorem ipsum dolor sit amet, consectetuer adipiscing elit, &nbsp;diam nonummy nibh euismod tincidunt...<b style="color:#fff">[+]</b></div>
<div class="abs avatar" style="left:100px;top:1980px" role="img" aria-label="Portrait photo of blog author"></div>
<div class="abs post-date" style="left:186px;top:1985px">Feb 18, 2016</div>
<div class="abs post-text" style="left:186px;top:2005px">Lorem ipsum dolor sit amet, consectetuer adipiscing elit, s diam nonummy nibh euismod tincidunt...<b style="color:#fff">[+]</b></div>
<div class="abs dots" style="left:497px;top:2070px"><i></i><i class="on"></i><i></i></div>

<div class="abs band-title caps" style="left:599px">What Client Say?</div>
<div class="abs band-rule" style="left:599px"></div>
<div class="abs quote-box">
  <div class="abs icon"><svg width="38" height="38" viewBox="0 0 38 38"><text x="19" y="27" text-anchor="middle" font-family="Georgia,serif" font-size="22" fill="#fff">“</text></svg></div>
  <div class="abs txt">Siam nonummy nibh euismod tincidunt ut laoreet do magna aliquam erat volutpat. Ut wisi enim ad minim veniam, &nbsp;v illum dolore eu feugiat nulla facilisis at vero eros et accumsan etL. iusto odio dig.</div>
</div>
<svg class="abs" style="left:640px;top:1996px" width="24" height="13" viewBox="0 0 24 13"><path d="M0 0.5L12 12L24 0.5" fill="#59524d" stroke="rgba(255,255,255,.75)"/></svg>
<div class="abs client-av" role="img" aria-label="Portrait photo of client"></div>
<div class="abs client-name">Nonummy Nibh</div>
<div class="abs dots" style="left:1038px;top:2070px"><i></i><i class="on"></i><i></i></div>

<!-- footer -->
<div class="abs footer"></div>
<div class="abs f-head caps" style="left:107px">About Us</div>
<div class="abs f-text" style="left:103px;top:2214px;width:290px">Proin gravida nibh vel velit auctor aliquet. Aenean sollicitudin, lorem quis bibendum auctor, nisi elit consequat ipsum, nec sagittis sem nibh id elit. Duis sed odio sit amet nibh</div>
<div class="abs social" style="left:104px"></div>
<div class="abs social" style="left:147px"></div>
<div class="abs social" style="left:190px"></div>
<div class="abs social" style="left:233px"></div>
<div class="abs f-div" style="left:421px"></div>

<div class="abs f-head caps" style="left:459px">Useful Links</div>
<ul class="abs f-links caps" style="left:459px;top:2212px">
  <li>About Us</li><li>Delivery Information</li><li>Privacy Policy</li><li>Terms &amp; Conditions</li><li>Contact Us</li><li>Returns</li><li>Site Map</li>
</ul>
<ul class="abs f-links caps" style="left:626px;top:2212px">
  <li>My Account</li><li>Order History</li><li>Wish List</li><li>Newsletter</li>
</ul>
<div class="abs f-div" style="left:752px"></div>

<div class="abs f-head caps" style="left:802px">Newsletter</div>
<div class="abs f-text" style="left:802px;top:2214px;width:300px">Duis sed odio sit amet nibh vulputate cursus a sit amet mauris.</div>
<div class="abs email">your email</div>
<div class="abs email-line"></div>
<div class="abs subscribe caps">Subscribe</div>

<!-- bottom bar -->
<div class="abs bottom"></div>
<div class="abs copy">Copyright © 2016 - <em>Velvethounds</em> - All rights reserved.</div>
<div class="abs pay" style="left:770px;background:#e8e8f0"></div>
<div class="abs pay" style="left:807px;background:#f0a030"></div>
<div class="abs pay" style="left:844px;background:#f4f0d8"></div>
<div class="abs pay" style="left:881px;background:#3f7fc4"></div>
<div class="abs pay" style="left:918px;background:#1f4f9a"></div>
<div class="abs pay" style="left:955px;background:#8a4fc4"></div>
<div class="abs pay" style="left:992px;background:#2a5fb0"></div>
<div class="abs pay" style="left:1029px;background:#e0c060"></div>
<div class="abs pay" style="left:1066px;background:#9b3a9b"></div>

</body>
</html>
```